Construction company featuring multiple photos to highlight work. Looking for clean modern design.

-Clean and modern design ****(SEE THUMBNAIL FILES FOR EASY PROJECT GROUPINGS)
-Looking for photos to be highlighted in a unique way to show before and after photos of Construction projects. (Please refer to this website for a possible layout . This is NOT our company but we like the layout of photos www.plovanstudio.com We dont want to copy any website but wanted to guide designers in the right direction.
will be uploading more content but looking for photo layout as a big part of the website design
******VERY IMPORTANT. Please see the 5 file uploads called THUMBNAILS for help with photo groups. this is to help you see the groups of photos that need to go together. (I have then uploaded the individual photos separately from thumbnail for better quality photos.)
****The photos that have been uploaded are labeled by room and house number(For example 3106 is a house number then it will say before or progress or after to show the project. . we would prefer to highlight projects by bathroom remodel, kitchen remodel, wood flooring and trim package jobs etc. NOT by house number. the house number was only to organize the photos not to list them on website by house number.
++++ Would like it to be very clear that the before photos are before construction begins.
++++Was maybe picturing small icons to show the before photos and a Larger slideshow showing the completed designs.
++++Feature photos would be the 3106 photos Kitchen/family room , bathrooms labeled 3106 is most current work.
++++Some photo catagories could be ....
-Kitchens Photos
-Bathrooms Photos
-Flooring/Doors/Trim Photos
-New Construction/Real Estate Renovations Photos
-Home Additions Photos
-Insurance Claims Fire and Water Damage Photos
-----Our Services:
-Remodeling Kitchen & Bath
-Insurance Claims Fire and Water Damage Repairs
-Home Additions / New Home Construction
-Flooring, tile, decking
-Custom built-ins and trim/door remodel
-Interior & Exterior Painting
-Roofing

Contact Us information:
Ashmoor Construction (Charleston South Carolina)
827 Tarrow Lane
Suite 415
Mount Pleasant, SC 29471
Owner: Dennis Roulard
Phone (803) 555-0147
Email: droulard@ashmoorbuild.com
Ashmoor Construction Website Content
-----Bio: Dennis Roulard, owner of Ashmoor Construction has over 17 years of experience working with customers on remodeling, renovation projects, and insurance related fire and water damage repairs.
----Contact us today to set up a free consultation.
(803) 555-0147
Will upload more text content soon

Industry/Entity Type

Residential General Contractor

Coding

Coded - Design and coding required

Requirements
Must have
• Ashmoor Construction Website Content Bio: Dennis Roulard, owner of Ashmoor Construction has over 17 years of experience working with customers on remodeling, renovation projects, and insurance related fire and water damage repairs. Contact us today to set up a free consultation. (803) 555-0147
Nice to have
• Nice to have a contact us page that can have a call now button with phone number or email. Would be really great if there could a way to have reviews populate from Verlo reviews.

```html
<!DOCTYPE html>
<html lang="en">
<head>
<meta charset="utf-8">
<title>Ashmoor Construction</title>
<link rel="stylesheet" href="https://fonts.googleapis.com/css2?family=Michroma&family=Jost:wght@400;500;600&display=swap">
<style>
:root{
  --blue:#5b9bd1;
  --ink:#2b2b2b;
  --text:#3a3a3a;
  --white:#ffffff;
  --cream:#f7f4f1;
  --black:#000000;
  --btn-dark:#3b3b3b;
  --muted:#6b6b6b;
  --display:"Michroma", sans-serif;
  --body:"Jost", sans-serif;
}
*{margin:0;padding:0;box-sizing:border-box}
html,body{width:1200px;height:4171px;overflow:hidden}
body{position:relative;font-family:var(--body);color:var(--text);background:var(--white)}
.abs{position:absolute}
a{color:inherit;text-decoration:none}

/* hero */
.hero{left:0;top:0;width:1200px;height:643px;overflow:hidden}
.hero-photo{position:absolute;inset:0;background:linear-gradient(180deg,#d9dee2 0%,#eef0f1 45%,#cfd4d8 100%)}
.nav-band{position:absolute;left:0;top:0;width:1200px;height:105px;background:rgba(255,255,255,.55)}
.brand{position:absolute;left:99px;top:34px;display:flex;align-items:center;gap:10px;font-family:var(--body);font-weight:600;font-size:22px;color:var(--ink);letter-spacing:.5px}
.brand-square{width:22px;height:22px;background:var(--blue)}
.nav-item{position:absolute;top:42px;font-size:15px;color:var(--ink);letter-spacing:.3px}
.nav-phone{position:absolute;left:939px;top:26px;width:161px;height:52px;background:var(--btn-dark);color:var(--white);font-size:16px;font-weight:600;display:flex;align-items:center;justify-content:center;gap:6px}
.hero-arrow{position:absolute;top:330px}
.hero-kicker{position:absolute;left:0;width:1200px;top:456px;text-align:center;font-family:var(--display);font-size:13px;letter-spacing:3px;color:var(--ink)}
.hero-big{position:absolute;left:0;width:1200px;top:488px;text-align:center;font-family:var(--display);font-size:64px;line-height:76px;color:var(--blue);letter-spacing:4px}
.hero-sub{position:absolute;left:0;width:1200px;top:566px;text-align:center;font-family:var(--display);font-size:28px;letter-spacing:14px;color:var(--ink)}

/* bio */
.bio-label{left:99px;top:802px;font-family:var(--display);font-size:15px;letter-spacing:4px;color:var(--ink)}
.bio-name{left:99px;top:828px;font-family:var(--display);font-size:30px;letter-spacing:2px;color:var(--ink)}
.bio-copy{left:99px;top:893px;width:400px;font-size:19px;line-height:30px;color:var(--text)}
.bio-cta{left:99px;top:1054px;font-size:17px;font-weight:600;color:var(--ink)}
.bio-phone{left:99px;top:1084px;font-size:24px;font-weight:500;color:var(--blue);display:flex;align-items:center;gap:10px;letter-spacing:1px}
.bio-photo{left:521px;top:737px;width:580px;height:465px;background:linear-gradient(135deg,#9a9a9a,#5e5e5e 60%,#c6c6c6)}

/* services */
.services{left:0;top:1320px;width:1200px;height:643px;background:var(--blue);color:var(--white)}
.services-title{position:absolute;left:0;width:1200px;top:68px;text-align:center;font-family:var(--display);font-size:40px;letter-spacing:4px}
.service{position:absolute;top:170px;width:330px;text-align:center}
.service-icon{width:88px;height:88px;margin:0 auto;border-radius:6px}
.service h3{margin-top:32px;font-size:18px;font-weight:500;line-height:27px;text-transform:uppercase}
.service p{margin-top:10px;font-size:17px;line-height:26px}
.service .more{display:inline-block;margin-top:20px;font-size:14px;font-weight:600;border-bottom:2px solid var(--white);padding-bottom:1px;letter-spacing:.5px}
.services-btn{position:absolute;left:494px;top:508px;width:210px;height:51px;border:2px solid var(--white);display:flex;align-items:center;justify-content:center;font-size:15px;font-weight:600;letter-spacing:.5px}

/* projects */
.projects-title{left:99px;top:2080px;font-family:var(--display);font-size:40px;letter-spacing:4px;color:var(--ink)}
.projects-btn{left:892px;top:2079px;width:211px;height:49px;border:2px solid #8a8a8a;display:flex;align-items:center;justify-content:center;font-size:15px;font-weight:500;color:var(--ink);letter-spacing:.5px}
.tab{position:absolute;font-size:17px;color:var(--ink)}
.tab.active{border-bottom:1px solid var(--ink)}
.pair{position:absolute;width:492px;height:352px;display:flex}
.pair .shot{position:relative;width:50%;height:100%}
.shot span{position:absolute;left:17px;bottom:14px;font-size:18px;font-weight:500;color:var(--ink)}

/* contact */
.contact{left:0;top:3153px;width:1200px;height:640px;background:var(--cream)}
.stay{left:99px;top:3262px;font-family:var(--display);font-size:17px;letter-spacing:2px;color:var(--ink)}
.touch{left:99px;top:3282px;font-family:var(--display);font-size:40px;letter-spacing:3px;color:var(--ink)}
.c-line{position:absolute;left:99px;font-size:18px;color:var(--ink)}
.c-company{color:var(--blue)}
.c-company em{font-style:normal;color:var(--muted)}
.c-owner{font-weight:600;font-size:20px}
.c-name{font-size:25px}
.c-icon{display:flex;align-items:center;gap:14px}
.contact-photo{left:578px;top:3260px;width:523px;height:429px;background:linear-gradient(180deg,#e5e7ea,#c9ccd0 55%,#b9a58e)}

/* footer */
.footer{left:0;top:3793px;width:1200px;height:378px;background:var(--black);color:var(--white)}
.f-brand{position:absolute;left:130px;top:130px;display:flex;align-items:center;gap:10px;font-weight:600;font-size:22px;color:var(--white)}
.f-brand .brand-square{background:var(--blue)}
.social{position:absolute;top:237px;width:14px;height:14px;border-radius:50%;background:var(--white)}
.f-rule{position:absolute;top:85px;width:1px;height:211px;background:#555}
.f-head{position:absolute;top:90px;font-family:var(--display);font-size:13px;letter-spacing:2px;color:var(--blue)}
.f-link{position:absolute;left:552px;font-size:14px;letter-spacing:.3px}
.f-input{position:absolute;left:845px;top:129px;width:256px;height:44px;border:1px solid var(--white);font-size:14px;display:flex;align-items:center;padding-left:14px}
.f-submit{position:absolute;left:845px;top:184px;width:256px;height:44px;background:var(--blue);display:flex;align-items:center;justify-content:center;font-size:14px;font-weight:600;letter-spacing:2px;color:var(--black)}
.f-copy{position:absolute;left:99px;top:341px;font-size:13px;color:#555}
.f-copy b{font-weight:400;color:var(--white)}
</style>
</head>
<body>

<header class="abs hero">
  <div class="hero-photo" role="img" aria-label="Bright white double-vanity bathroom with grey tile floor"></div>
  <div class="nav-band"></div>
  <div class="brand"><span class="brand-square"></span>Ashmoor Construction</div>
  <a class="nav-item" style="left:413px">HOME</a>
  <a class="nav-item" style="left:492px">ABOUT ME</a>
  <a class="nav-item" style="left:601px">OUR SERVICES</a>
  <a class="nav-item" style="left:737px">PORTFOLIO</a>
  <a class="nav-item" style="left:849px">CONTACT</a>
  <a class="nav-phone">
    <svg width="14" height="14" viewBox="0 0 24 24"><path fill="#fff" d="M6.6 10.8a15.1 15.1 0 0 0 6.6 6.6l2.2-2.2c.3-.3.7-.4 1-.2 1.1.4 2.3.6 3.6.6.6 0 1 .4 1 1V20c0 .6-.4 1-1 1A17 17 0 0 1 3 4c0-.6.4-1 1-1h3.5c.6 0 1 .4 1 1 0 1.3.2 2.5.6 3.6.1.3 0 .7-.2 1z"/></svg>
    (803) 555-0147</a>
  <svg class="hero-arrow" style="left:100px" width="26" height="52" viewBox="0 0 26 52"><path d="M24 2 2 26l22 24" fill="none" stroke="#333" stroke-width="2"/></svg>
  <svg class="hero-arrow" style="left:1075px" width="26" height="52" viewBox="0 0 26 52"><path d="M2 2l22 24L2 50" fill="none" stroke="#333" stroke-width="2"/></svg>
  <p class="hero-kicker">ASHMOOR CONSTRUCTION HAS OVER</p>
  <h1 class="hero-big">17 YEARS</h1>
  <p class="hero-sub">OF EXPERIENCE</p>
</header>

<section>
  <p class="abs bio-label">BIO</p>
  <h2 class="abs bio-name">DENNIS ROULARD</h2>
  <p class="abs bio-copy">Dennis Roulard, owner of Ashmoor Construction has over 17 years of experience working with customers on remodeling, renovation projects, and insurance related fire and water damage repairs.</p>
  <p class="abs bio-cta">Contact us today to set up a free consultation.</p>
  <p class="abs bio-phone">
    <svg width="20" height="20" viewBox="0 0 24 24"><path fill="#5b9bd1" d="M6.6 10.8a15.1 15.1 0 0 0 6.6 6.6l2.2-2.2c.3-.3.7-.4 1-.2 1.1.4 2.3.6 3.6.6.6 0 1 .4 1 1V20c0 .6-.4 1-1 1A17 17 0 0 1 3 4c0-.6.4-1 1-1h3.5c.6 0 1 .4 1 1 0 1.3.2 2.5.6 3.6.1.3 0 .7-.2 1z"/></svg>
    (803) 555-0147</p>
  <div class="abs bio-photo" role="img" aria-label="Black and white family portrait of the owner outdoors"></div>
</section>

<section class="abs services">
  <h2 class="services-title">OUR SERVICES</h2>
  <div class="service" style="left:86px">
    <div class="service-icon" role="img" aria-label="House remodel illustration" style="background:linear-gradient(135deg,#e9eef5,#c9455a)"></div>
    <h3>Remodeling Kitchen &amp; Bath</h3>
    <p>Phasellus quis justo lectus. Cras tincidunt leo non ornare sollicitudin. Vestibulum auctor vitae orci eget imperdiet.</p>
    <a class="more">READ MORE</a>
  </div>
  <div class="service" style="left:433px">
    <div class="service-icon" role="img" aria-label="Insurance claim clipboard illustration" style="background:linear-gradient(135deg,#3d3d3d,#f0f0f0)"></div>
    <h3>Insurance Claims Fire and<br>Water Damage Repairs</h3>
    <p>Phasellus quis justo lectus. Cras tincidunt leo non ornare sollicitudin.</p>
    <a class="more">READ MORE</a>
  </div>
  <div class="service" style="left:781px">
    <div class="service-icon" role="img" aria-label="Tiled floor room illustration" style="background:linear-gradient(180deg,#d7dbe4,#a9604a)"></div>
    <h3>Flooring, Tile, Decking</h3>
    <p>Phasellus quis justo lectus. Cras tincidunt leo non ornare sollicitudin. Vestibulum auctor vitae orci eget imperdiet.</p>
    <a class="more">READ MORE</a>
  </div>
  <a class="services-btn">VIEW ALL SERVICES</a>
</section>

<section>
  <h2 class="abs projects-title">RECENT PROJECT</h2>
  <a class="abs projects-btn">VIEW ALL PROJECTS</a>
  <a class="tab active" style="left:99px;top:2165px">Kitchens</a>
  <a class="tab" style="left:203px;top:2165px">Bathrooms</a>
  <a class="tab" style="left:325px;top:2165px">Flooring/Doors/Trim</a>
  <a class="tab" style="left:525px;top:2165px">New Construction/Real Estate Renovations</a>
  <a class="tab" style="left:99px;top:2208px">Home Additions</a>
  <a class="tab" style="left:263px;top:2208px">Insurance Claims Fire and Water Damage</a>

  <div class="pair" style="left:99px;top:2283px">
    <div class="shot" role="img" aria-label="Laundry room before renovation" style="background:linear-gradient(180deg,#dcdfe2,#bfc3c6)"><span>BEFORE</span></div>
    <div class="shot" role="img" aria-label="Renovated white laundry room" style="background:linear-gradient(180deg,#f1f0ec,#cdb99a)"><span>AFTER</span></div>
  </div>
  <div class="pair" style="left:609px;top:2283px">
    <div class="shot" role="img" aria-label="Dining room with worn wood floor before renovation" style="background:linear-gradient(180deg,#e6e2dc,#243040 45%,#6a3f22)"><span>BEFORE</span></div>
    <div class="shot" role="img" aria-label="Renovated dining room with table and pendant light" style="background:linear-gradient(180deg,#f2f2f0,#c9c6c0 60%,#9b7f5e)"><span>AFTER</span></div>
  </div>
  <div class="pair" style="left:99px;top:2670px">
    <div class="shot" role="img" aria-label="Older kitchen with granite counters before renovation" style="background:linear-gradient(180deg,#ece8df,#c9ad7c 60%,#5a4b3a)"><span>BEFORE</span></div>
    <div class="shot" role="img" aria-label="Renovated white kitchen with island" style="background:linear-gradient(180deg,#f4f3f0,#e0ddd6 60%,#b89a72)"><span>AFTER</span></div>
  </div>
  <div class="pair" style="left:609px;top:2670px">
    <div class="shot" role="img" aria-label="Kitchen framing during construction" style="background:linear-gradient(180deg,#c9ad84,#9c7a52 60%,#6b5a48)"><span>BEFORE</span></div>
    <div class="shot" role="img" aria-label="Finished kitchen with range hood and copper pendants" style="background:linear-gradient(180deg,#f5f5f3,#dcdcd8 60%,#b7a58a)"><span>AFTER</span></div>
  </div>
</section>

<section class="abs contact"></section>
<p class="abs stay">STAY IN</p>
<h2 class="abs touch">TOUCH</h2>
<p class="c-line c-company" style="top:3348px">Ashmoor Construction <em>(Charleston South Carolina)</em></p>
<p class="c-line" style="top:3375px">827 Tarrow Lane</p>
<p class="c-line" style="top:3401px">Suite 415</p>
<p class="c-line" style="top:3428px">Mount Pleasant, SC 29471</p>
<p class="c-line c-owner" style="top:3466px">Owner</p>
<p class="c-line c-name" style="top:3503px">Dennis Roulard</p>
<p class="c-line c-icon" style="top:3552px">
  <svg width="18" height="18" viewBox="0 0 24 24"><path fill="#5b9bd1" d="M6.6 10.8a15.1 15.1 0 0 0 6.6 6.6l2.2-2.2c.3-.3.7-.4 1-.2 1.1.4 2.3.6 3.6.6.6 0 1 .4 1 1V20c0 .6-.4 1-1 1A17 17 0 0 1 3 4c0-.6.4-1 1-1h3.5c.6 0 1 .4 1 1 0 1.3.2 2.5.6 3.6.1.3 0 .7-.2 1z"/></svg>
  (803) 555-0147</p>
<p class="c-line c-icon" style="top:3589px">
  <svg width="18" height="14" viewBox="0 0 18 14"><rect width="18" height="14" rx="1" fill="#5b9bd1"/><path d="M1 1l8 6 8-6" fill="none" stroke="#fff" stroke-width="1.5"/></svg>
  droulard@ashmoorbuild.com</p>
<div class="abs contact-photo" role="img" aria-label="Renovated home office with desk and built-in shelving"></div>

<footer class="abs footer">
  <div class="f-brand"><span class="brand-square"></span>Ashmoor Construction</div>
  <span class="social" style="left:140px"></span>
  <span class="social" style="left:184px"></span>
  <span class="social" style="left:233px"></span>
  <span class="social" style="left:283px"></span>
  <span class="f-rule" style="left:421px"></span>
  <span class="f-rule" style="left:781px"></span>
  <p class="f-head" style="left:552px">QUICK LINKS</p>
  <a class="f-link" style="top:128px">HOME</a>
  <a class="f-link" style="top:162px">ABOUT ME</a>
  <a class="f-link" style="top:196px">OUR SERVICES</a>
  <a class="f-link" style="top:231px">PORTFOLIO</a>
  <a class="f-link" style="top:265px">CONTACT</a>
  <p class="f-head" style="left:845px">QUICK LINKS</p>
  <div class="f-input">Enter your email here*</div>
  <div class="f-submit">SUBSCRIBE</div>
  <p class="f-copy">© 2023 <b>Ashmoor Construction</b> All right reserved</p>
</footer>

</body>
</html>
```